Update Business Card Design Project

We've been in business nearly 15 years and about 10 years ago developed a brand that is now well recognized. The business card is boring, too much print and nothing that says 'We are SIMPLY SPLENDID' right off the mark.
We are a fun store, lots of new things on a regular basis. Especially in kitchen goods where the colours are strong and the emphasis is on pretty and practical. We like to have both!
Hi there,
Target Market(s)
Store customers and suppliers
Demographics aged 40-70yrs, mid to high income, mostly women or couples, rural setting but in the 'shopping district' of our region. 1 hour to nearest city.
Industry/Entity Type
Business
Requirements
Nice to have
- Incorporate the logo, if possible

```html
<!DOCTYPE html>
<html lang="en">
<head>
<meta charset="utf-8">
<title>Simply Splendid – Business Cards</title>
<link href="https://fonts.googleapis.com/css2?family=Jura:wght@400;500&family=Michroma&display=swap" rel="stylesheet">
<style>
  :root {
    --bg: #e9e9e9;
    --card: #e6e6e6;
    --brand: #8a4a10;
    --ink: #2e2e2e;
    --accent: #b86a1c;
    --faint: #cfcfcf;
    --blue-light: #2aa6dc;
    --blue-dark: #1b5f8e;
    --white: #ffffff;
    --shadow: rgba(0, 0, 0, 0.30);
  }
  * { margin: 0; padding: 0; box-sizing: border-box; }
  html, body { width: 1200px; height: 1069px; overflow: hidden; background: var(--bg); }
  .sheet { position: relative; width: 1200px; height: 1069px; }
  .card {
    position: absolute; background: var(--card); overflow: hidden;
    box-shadow: 0 10px 22px var(--shadow), 0 2px 5px rgba(0, 0, 0, 0.15);
  }
  .front-a { left: 78px; top: 178px; width: 429px; height: 246px; }
  .back-a  { left: 691px; top: 185px; width: 417px; height: 239px; }
  .front-b { left: 97px; top: 680px; width: 428px; height: 245px; }
  .back-b  { left: 709px; top: 688px; width: 417px; height: 237px; }

  .brand {
    position: absolute; left: 0; right: 0; top: 50%;
    transform: translateY(-50%);
    display: flex; align-items: center; justify-content: center; gap: 12px;
  }
  .brand-mark { width: 22px; height: 22px; background: var(--brand); }
  .brand-name {
    font-family: "Michroma", sans-serif; font-size: 20px;
    color: var(--brand); letter-spacing: 1px; text-transform: uppercase;
  }

  .deco-square {
    position: absolute; right: 20px; top: 10px; width: 96px; height: 96px;
    border: 8px solid var(--faint);
  }
  .holder { position: absolute; left: 27px; top: 38px; }
  .holder-name {
    font-family: "Jura", sans-serif; font-weight: 500; font-size: 26px;
    color: var(--brand); line-height: 1;
  }
  .holder-title {
    font-family: "Jura", sans-serif; font-size: 14px; color: var(--ink);
    margin-left: 122px; margin-top: 4px;
  }
  .details {
    position: absolute; left: 32px; top: 142px;
    font-family: "Jura", sans-serif; font-size: 11.5px; line-height: 15px; color: var(--ink);
  }
  .details .val { color: var(--accent); }
  .details .indent { padding-left: 60px; }
  .details .row { margin-bottom: 6px; }
  .details .row:last-child { margin-bottom: 0; }
  .back-b .details { top: 100px; }
  .back-b .details .val { color: var(--ink); }

  .wave { position: absolute; left: 0; bottom: 0; width: 417px; height: 110px; }
  .site {
    position: absolute; left: 0; right: 0; bottom: 8px; text-align: center;
    font-family: "Michroma", sans-serif; font-size: 15px; color: var(--white);
    letter-spacing: 1px; padding-left: 20px;
  }
</style>
</head>
<body>
<main class="sheet">

  <section class="card front-a">
    <div class="brand">
      <span class="brand-mark"></span>
      <span class="brand-name">Simply Splendid</span>
    </div>
  </section>

  <section class="card back-a">
    <div class="deco-square"></div>
    <div class="holder">
      <p class="holder-name">Daniel Harrow</p>
      <p class="holder-title">President</p>
    </div>
    <div class="details">
      <div class="row">Address: <span class="val">Maple Court Plaza 4215 Harbour Street</span><br>
        <span class="val indent">Port Elden, Nova Scotia, B2X 5K7</span></div>
      <div class="row">Telephone # <span class="val">1 800 555 0147</span><br>
        <span class="val indent">902 555 0183</span></div>
      <div class="row">Website: <span class="val">www.simplysplendid.ca</span></div>
    </div>
  </section>

  <section class="card front-b">
    <div class="brand">
      <span class="brand-mark"></span>
      <span class="brand-name">Simply Splendid</span>
    </div>
  </section>

  <section class="card back-b">
    <svg class="wave" viewBox="0 0 417 110" preserveAspectRatio="none" aria-hidden="true">
      <defs>
        <linearGradient id="waveFill" x1="0" y1="1" x2="1" y2="0">
          <stop offset="0" stop-color="#1b5f8e"/>
          <stop offset="0.55" stop-color="#2aa6dc"/>
          <stop offset="1" stop-color="#1b5f8e"/>
        </linearGradient>
      </defs>
      <path d="M0 60 C120 46 260 28 417 18 L417 110 L0 110 Z" fill="url(#waveFill)"/>
      <path d="M0 60 C90 76 200 96 320 110 L0 110 Z" fill="#1b5f8e" opacity="0.55"/>
    </svg>
    <div class="deco-square"></div>
    <div class="holder">
      <p class="holder-name">Daniel Harrow</p>
      <p class="holder-title">President</p>
    </div>
    <div class="details">
      <div class="row">Address: <span class="val">Maple Court Plaza 4215 Harbour Street</span><br>
        <span class="val indent">Port Elden, Nova Scotia, B2X 5K7</span></div>
      <div class="row">Telephone # <span class="val">1 800 555 0147</span><br>
        <span class="val indent">902 555 0183</span></div>
    </div>
    <p class="site">www.simplysplendid.ca</p>
  </section>

</main>
</body>
</html>
```